Edit and Update existing catalog

I have a 60 paged catalog that needs to have some changes. We are adding around 20 pages, changing another 15 pages, and also have 10 pages that need to be graphically designed and inserted. The current existing catalog is included as well as a PDF explaining all the changes (Catalog Changes.pdf), as well as all the pages that need to be added and our logo.

Target Market(s)

physician offices and professional healthcare providers

Industry/Entity Type

Healthcare

Colors
0054AA
0677BA
7BADD7
CADEEF
E8F1F8

Requirements
Must have
• Additional pages must match the format of the existing catalog
Should not have
• No protected health information - all patient names, Date of births and accession #s should be removed, incase they are not please replace with XXX on the reports.

```html
<!DOCTYPE html>
<html lang="en">
<head>
<meta charset="utf-8">
<title>New Tox Report</title>
<link href="https://fonts.googleapis.com/css2?family=Tinos:ital,wght@0,400;0,700;1,700&family=Open+Sans:wght@400;600;700&display=swap" rel="stylesheet">
<style>
:root{
  --brand:#0677BA;
  --brand-dark:#0054AA;
  --ink:#111;
  --rule:#555;
  --head:#d9d9d9;
  --pos:#1f9a1f;
  --neg:#e0201e;
  --tab:#5a5a5a;
}
*{box-sizing:border-box;margin:0;padding:0}
html,body{width:982px;height:1200px;overflow:hidden;background:#fff}
body{position:relative;font-family:"Tinos",serif;color:var(--ink)}
.page{position:absolute;left:0;top:0;width:915px;height:1200px}
.tab-strip{position:absolute;right:0;top:0;width:67px;height:1200px;background:var(--tab)}
.tab-label{position:absolute;right:8px;top:445px;width:50px;height:480px;display:flex;align-items:center;justify-content:center}
.tab-label span{transform:rotate(90deg);white-space:nowrap;color:#fff;font-family:"Open Sans",sans-serif;font-size:16px}
.title{position:absolute;top:18px;left:0;width:915px;text-align:center;color:var(--brand);font-weight:700;font-size:31px;letter-spacing:.5px}
.title::after{content:"";display:block;width:290px;height:2px;background:var(--brand);margin:2px auto 0}
.brand{position:absolute;left:60px;top:96px;display:flex;align-items:center;gap:8px;font-family:"Open Sans",sans-serif;font-weight:700;font-size:15px;line-height:17px;color:var(--brand-dark)}
.brand i{display:block;flex:none;width:22px;height:22px;border-radius:50%;background:var(--brand)}
.brand-rule{position:absolute;left:232px;top:68px;width:1px;height:75px;background:#bbb}
.contact{position:absolute;left:258px;top:68px;font-family:"Open Sans",sans-serif;font-size:12px;line-height:18px;color:#333}
.contact div{display:flex;align-items:flex-start;gap:7px}
.contact svg{flex:none;margin-top:3px}
.director{position:absolute;left:505px;top:104px;font-family:"Open Sans",sans-serif;font-size:12px;line-height:20px;color:#333}
.director b{font-weight:600}
.head-rule{position:absolute;left:60px;top:151px;width:824px;height:1.5px;background:#333}
.patient{position:absolute;left:60px;top:163px;width:824px;font-size:13px;line-height:19px}
.patient .c{position:absolute;top:0}
.report-name{position:absolute;top:231px;left:0;width:915px;text-align:center;font-weight:700;font-size:17px;text-decoration:underline}
.meds{position:absolute;top:270px;left:68px;width:816px;font-size:11px;font-weight:700;display:flex;justify-content:space-between}
.meds em{font-style:italic}
.section{position:absolute;left:63px;width:818px}
.section h2{font-size:11.5px;font-weight:700;margin-bottom:5px}
table{width:100%;border-collapse:collapse;font-size:10.5px}
th,td{border:1px solid var(--rule);padding:0 4px;height:18px;line-height:12px}
th{background:var(--head);font-weight:700;text-align:center;height:23px}
td.c{text-align:center}
.pos{color:var(--pos)}
.neg{color:var(--neg)}
.r th{height:30px}
.footer{position:absolute;left:63px;top:1098px;width:818px;border-top:1px solid #333;font-size:11px;line-height:16px;padding-top:5px}
.footer .right{position:absolute;right:0;top:5px;text-align:right}
.footer .status{text-align:center;margin-top:4px;margin-left:60px}
.page-no{position:absolute;left:880px;top:1160px;font-family:"Open Sans",sans-serif;font-size:12px}
</style>
</head>
<body>
<div class="page">
  <h1 class="title">NEW TOX REPORT</h1>

  <div class="brand"><i></i><span>HARBOR POINT<br>LABS</span></div>
  <div class="brand-rule"></div>
  <div class="contact">
    <div><svg width="10" height="12" viewBox="0 0 10 12"><path d="M5 0a4 4 0 0 0-4 4c0 3 4 8 4 8s4-5 4-8a4 4 0 0 0-4-4z" fill="var(--brand)"/></svg><span>1450 Lakeview Pkwy<br>Suite 200, Maplewood, MI 48099</span></div>
    <div><svg width="11" height="11" viewBox="0 0 11 11"><path d="M2 0l2 3-1 1.5c.8 1.6 1.9 2.7 3.5 3.5L8 7l3 2-1 2C5 11 0 6 0 1z" fill="var(--brand)"/></svg><span>(555) 240-7182</span></div>
    <div><svg width="11" height="11" viewBox="0 0 11 11"><circle cx="5.5" cy="5.5" r="4.5" fill="none" stroke="var(--brand)" stroke-width="1.4"/></svg><span>harborpointlabs.test</span></div>
  </div>
  <div class="director">
    <div>LAB DIRECTOR <b>Dana Whitfield, MD</b></div>
    <div><b>CLIA ID#</b> 00D0000000</div>
  </div>
  <div class="head-rule"></div>

  <div class="patient">
    <div class="c" style="left:0"><b>XXX</b><br>1450 LAKEVIEW PKWY<br>Maplewood, MI 48099</div>
    <div class="c" style="left:243px"><b>TEST, TOXICOLOGY</b></div>
    <div class="c" style="left:243px;top:19px;font-size:11px;line-height:19px">Patient #:<br>DOB:</div>
    <div class="c" style="left:308px;top:19px">XXX<br>XXX</div>
    <div class="c" style="left:395px;top:19px;font-size:11px;line-height:19px">MRN:<br>Sex:</div>
    <div class="c" style="left:440px;top:21px;line-height:19px"><br>Male</div>
    <div class="c" style="left:550px;font-size:11px">Accession:<br>Collected:<br>Approved:</div>
    <div class="c" style="left:633px">XXX<br>3/16/2024 9:08 AM &nbsp;&nbsp;&nbsp;RK<br>3/18/2024 8:11 PM</div>
  </div>

  <div class="report-name">Drug Adherence Assessment Report</div>
  <div class="meds"><span>Medications: &nbsp;&nbsp;&nbsp;<em>Alprazolam [Calmex ], Amphetamine [Focusyn], Hydrocodone [Dolvera]</em></span><span>Listed Medications Not Tested For: &nbsp;&nbsp;<em>None</em></span></div>

  <section class="section" style="top:318px">
    <h2>URINE DRUG SCREEN SUMMARY</h2>
    <table>
      <tr><th style="width:22%">TEST NAME</th><th style="width:26%">RESULT</th><th style="width:7%">UNITS</th><th style="width:13%">FLAG</th><th>REFERENCE RANGE/CUTOFF</th></tr>
      <tr><td>Amphetamine</td><td class="c">POSITIVE</td><td></td><td class="c">POSITIVE</td><td class="c">&lt;500</td></tr>
      <tr><td>Benzodiazepine</td><td class="c">POSITIVE</td><td></td><td class="c">POSITIVE</td><td class="c">&lt;200</td></tr>
      <tr><td>Marijuana (THC)</td><td class="c">POSITIVE</td><td></td><td class="c">POSITIVE</td><td class="c">&lt;50</td></tr>
    </table>
  </section>

  <section class="section" style="top:444px">
    <h2>PRESCRIBED MEDICATIONS</h2>
    <table>
      <tr class="r"><th style="width:16%">REPORTED<br>PRESCRIPTIONS</th><th style="width:17%">ANTICIPATED<br>POSITIVES</th><th style="width:12%">MEASURED<br>RESULTS</th><th style="width:7%">CUTOFF</th><th style="width:10%">TEST<br>OUTCOME</th><th style="width:17%">COMMENTS</th><th>DETECTION<br>WINDOW</th></tr>
      <tr class="pos"><td rowspan="2">Alprazolam [Calmex ]</td><td>Alprazolam</td><td class="c">67</td><td class="c">25</td><td class="c">POSITIVE</td><td class="c neg">Consistent</td><td class="c neg">1-4</td></tr>
      <tr class="pos"><td>Alpha-hydroxyalprazolam</td><td class="c">90</td><td class="c">25</td><td class="c">POSITIVE</td><td class="c neg">Consistent</td><td class="c neg">2-3</td></tr>
      <tr class="pos"><td>Amphetamine [Focusyn]</td><td>Amphetamine</td><td class="c">110</td><td class="c">50</td><td class="c">POSITIVE</td><td class="c neg">Consistent</td><td class="c neg">1-3</td></tr>
      <tr class="neg"><td rowspan="3">Hydrocodone [Dolvera]</td><td>Hydrocodone</td><td class="c">N/A</td><td class="c">25</td><td class="c">NEGATIVE</td><td class="c">Inconsistent</td><td class="c">3-4</td></tr>
      <tr class="neg"><td>Norhydrocodone</td><td class="c">N/A</td><td class="c">25</td><td class="c">NEGATIVE</td><td class="c">Inconsistent</td><td class="c">2-4</td></tr>
      <tr class="neg"><td>Hydromorphone</td><td class="c">N/A</td><td class="c">25</td><td class="c">NEGATIVE</td><td class="c">Inconsistent</td><td class="c">2-3</td></tr>
    </table>
  </section>

  <section class="section" style="top:625px">
    <h2>INCONSISTENT RESULTS - ANALYTE DETECTED BUT NO CORRESPONDING PRESCRIPTION REPORTED</h2>
    <table>
      <tr class="r"><th style="width:20%">ANALYTE DETECTED</th><th style="width:14%">ILLICIT</th><th style="width:10%">MEASURED<br>RESULT</th><th style="width:6%">CUTOFF</th><th style="width:22%">TEST OUTCOME</th><th>DETECTION WINDOW</th></tr>
      <tr class="neg"><td>THC-COOH</td><td class="c">Yes</td><td class="c">125</td><td class="c">12.5</td><td class="c">POSITIVE</td><td class="c">1-3</td></tr>
      <tr class="neg"><td>Clonazepam</td><td class="c">No</td><td class="c">65</td><td class="c">20</td><td class="c">POSITIVE</td><td class="c">2-7</td></tr>
      <tr class="neg"><td>7-aminoclonazepam</td><td class="c">No</td><td class="c">100</td><td class="c">25</td><td class="c">POSITIVE</td><td class="c">2-7</td></tr>
    </table>
  </section>

  <section class="section" style="top:762px">
    <h2>SPECIMEN VALIDITY TESTING</h2>
    <table>
      <tr><th style="width:26%;text-align:left">TEST</th><th style="width:21%">MEASURED RESULT</th><th style="width:16%">TEST OUTCOME</th><th>REFERENCE RANGE</th></tr>
      <tr><td>Creatinine</td><td class="c">25.00</td><td class="c">Normal</td><td class="c">20.00 - 400.00</td></tr>
      <tr><td>pH</td><td class="c">5.00</td><td class="c">Normal</td><td class="c">4.50 - 9.00</td></tr>
      <tr><td>Specific Gravity</td><td class="c">1.005</td><td class="c">Normal</td><td class="c">1.002 - 1.030</td></tr>
    </table>
  </section>

  <section class="section" style="top:878px">
    <h2>HISTORICAL REPORT</h2>
    <table>
      <tr><th style="width:20%;text-align:left;height:18px">Analyte</th><th style="height:18px">1/18/2024</th><th style="height:18px">12/19/2023</th><th style="height:18px">11/19/2023</th><th style="height:18px">10/19/2023</th><th style="height:18px">9/19/2023</th></tr>
      <tr><td>Alprazolam</td><td class="c">75</td><td class="c">N/A</td><td class="c">65</td><td class="c">N/A</td><td class="c">35</td></tr>
      <tr><td>Alpha-hydroxyalprazolam</td><td class="c">78</td><td class="c">86</td><td class="c">76</td><td class="c">75</td><td class="c">45</td></tr>
      <tr><td>Amphetamine</td><td class="c">890</td><td class="c">780</td><td class="c">926</td><td class="c">118</td><td class="c">812</td></tr>
      <tr><td>Clonazepam</td><td class="c"><b>65</b></td><td class="c">65</td><td class="c">45</td><td class="c">45</td><td class="c">34</td></tr>
      <tr><td>7-aminoclonazepam</td><td class="c"><b>105</b></td><td class="c"><b>65</b></td><td class="c">65</td><td class="c">65</td><td class="c">76</td></tr>
      <tr><td>Hydrocodone</td><td class="c">N/A</td><td class="c">150</td><td class="c">200</td><td class="c">100</td><td class="c">80</td></tr>
      <tr><td>Norhydrocodone</td><td class="c">500</td><td class="c">N/A</td><td class="c">100</td><td class="c">50</td><td class="c">21</td></tr>
      <tr><td>Hydromorphone</td><td class="c">50</td><td class="c">N/A</td><td class="c">125</td><td class="c">50</td><td class="c">47</td></tr>
      <tr><td>THC-COOH</td><td class="c">125</td><td class="c">65</td><td class="c">415</td><td class="c">200</td><td class="c">76</td></tr>
    </table>
  </section>

  <footer class="footer">
    <div>Originally Printed On: 3/18/2024 8:11 PM</div>
    <div>Printed: 3/19/2024 9:03 AM</div>
    <div class="right">Accession: XXX &nbsp;&nbsp;Patient #: XXX<br>Lab Results for: TEST, TOXICOLOGY</div>
    <div class="status">STAT[S] Corrected [C] Amended [A]</div>
  </footer>
  <div class="page-no">5</div>
</div>

<aside class="tab-strip">
  <div class="tab-label"><span>Tabs Here - This portion will be trimmed off</span></div>
</aside>
</body>
</html>
```